Re-design an HTML Website

Website must be responsive/fluid and designed with mobile-first priority. I want to be able to make changes with a HTML editor

We offer EMF Protection devices that neutralize EMF radiations emitted from electronics. We have devices for people and cell phones.
.

Redesign our Website (www.brightpebs.us) to look more modern, but I need to keep it in an HTML format. I plan on keeping the same shopping cart service (WareCrate.com), as it has some features we need, but it is BUTTON intensive.

Requirements requested (samples submitted):
Headers and Footers
Menu setup as submitted
Creative Landing Page
Categories Page (must be stacked products)
Products Page (must be stacked products)
Individual Product Page
Generic 1-Column Page
Generic 2-Column Page
Generic 3-Column Page
Updates

What we sell are devices to neutralize the electromagnetic radiation (EMF) emitted from cell phones and electronics. Anything thing you can do to bring this website (www.BrightPEBs.us) into the 21st Century will be appreciated. It is a secondary website for our Affiliate Accounts - our primary site is at Vendora www.TopWaveGoods.com

Be creative -- make us look and feel great!

Thanks, Dorian

Providing both a Mobile & Desktop screen shot would be helpful.

Also, do not use the products from pulsebeads.com - it is a slightly different product.
www.TopWaveGoods.com or www.BrightPEBs.us are our product configurations.

Industry/Entity Type

Technologoy

Coding

Coded - Design and coding required

Number of Pages Required

5+ page

Requirements
Must have
• Zip file and desciptions included
Nice to have
• Menu / footer /header / Landing page / Product Page / Category Page

```html
<!DOCTYPE html>
<html lang="en">
<head>
<meta charset="utf-8">
<title>Top Wave Goods — EMF Products</title>
<link rel="stylesheet" href="https://fonts.googleapis.com/css2?family=Bebas+Neue&family=Poppins:wght@400;500;600;700&display=swap">
<style>
:root{
  --blue:#2f80cf;
  --blue-dark:#2468ad;
  --ink:#1c1c1c;
  --muted:#5c5c5c;
  --line:#d9d9d9;
  --footer:#222222;
  --footer-deep:#1a1a1a;
  --star:#f39c1f;
  --white:#ffffff;
}
*{box-sizing:border-box;margin:0;padding:0}
html,body{width:1200px;height:3456px;overflow:hidden}
body{font-family:"Poppins",sans-serif;color:var(--ink);background:var(--white);position:relative}
.display{font-family:"Bebas Neue",sans-serif;font-weight:400;letter-spacing:.3px}
.abs{position:absolute}
.btn{display:inline-flex;align-items:center;justify-content:center;gap:8px;background:var(--blue);color:var(--white);font-size:10px;font-weight:600;text-transform:uppercase;letter-spacing:.2px}

/* top bar */
.topbar{top:0;left:0;width:1200px;height:23px;background:#f1f1f1;font-size:9px;font-weight:500;display:flex;align-items:center;justify-content:space-between;padding:0 88px}
.topbar span{display:inline-flex;align-items:center;gap:5px}
/* header */
.header{top:23px;left:0;width:1200px;height:56px;display:flex;align-items:center;padding:0 88px}
.wordmark{font-family:"Poppins",sans-serif;font-weight:600;font-size:21px;line-height:1;color:var(--ink);white-space:nowrap}
.search{position:absolute;left:418px;top:15px;width:469px;height:30px;border:1px solid #8a8a8a;display:flex;font-size:11px;color:#9a9a9a}
.search .cat{width:146px;border-right:1px solid #8a8a8a;display:flex;align-items:center;justify-content:space-between;padding:0 10px}
.search .field{flex:1;display:flex;align-items:center;padding:0 14px}
.search .go{width:40px;border-left:1px solid #8a8a8a;display:flex;align-items:center;justify-content:center}
.icons{position:absolute;right:88px;top:18px;display:flex;gap:22px}
/* nav */
.nav{top:79px;left:0;width:1200px;height:36px;background:var(--blue);display:flex;align-items:center;justify-content:center;gap:48px;color:var(--white);font-size:11.5px;font-weight:500;padding-right:60px}
.nav .active{font-weight:700}
/* hero */
.hero{top:115px;left:0;width:1200px;height:473px;background:linear-gradient(100deg,#e9e9e9 0%,#dcdcdc 45%,#8fa58a 70%,#7f9678 100%)}
.hero-kicker{left:88px;top:246px;color:var(--blue);font-size:17px;font-weight:600;letter-spacing:.3px}
.hero-title{left:86px;top:272px;font-size:84px;line-height:1}
.hero-text{left:89px;top:357px;width:370px;font-size:13px;line-height:1.25;color:#333}
.hero-btn{left:88px;top:408px;width:163px;height:36px;font-size:10.5px}
.hero-dots{left:568px;top:560px;display:flex;gap:4px;align-items:center}
.hero-dots i{width:5px;height:5px;border-radius:50%;background:var(--blue)}
.hero-dots b{width:32px;height:5px;border-radius:3px;background:var(--white)}
/* features */
.features{top:637px;left:0;width:1200px;height:81px;display:flex;justify-content:center}
.feature{display:flex;align-items:center;gap:10px;padding:0 64px}
.feature + .feature{border-left:1px solid #bdbdbd}
.feature h4{font-size:20px;line-height:1}
.feature p{font-size:7.5px;color:var(--muted)}
/* section titles */
.sec-title{left:0;width:1200px;text-align:center;font-size:44px;line-height:1}
.sec-rule{left:560px;width:82px;height:3px;background:var(--blue)}
/* categories */
.cat-card{top:851px;width:240px;height:295px;border:1.5px solid #4a4a4a;display:flex;align-items:center;justify-content:center}
.cat-pack{width:89px;height:220px}
.cat-name{top:1172px;width:240px;text-align:center;font-size:31px}
.explore{left:535px;top:1245px;width:131px;height:37px}
/* starter packages */
.pack{top:1420px;height:339px;color:var(--white)}
.pack .inner{position:absolute;left:236px;top:62px;width:330px}
.pack h3{font-size:34px;line-height:1}
.pack .price{font-size:28px;margin-top:10px;line-height:1}
.pack .price s{font-family:"Poppins",sans-serif;font-size:11px;font-weight:600}
.pack ul{margin:14px 0 0 14px;font-size:13.5px;line-height:1.25}
.pack li{margin-bottom:4px}
.pack .add{position:absolute;left:0;top:228px;width:153px;height:37px;background:var(--white);color:var(--ink);font-size:10px;font-weight:600;display:flex;align-items:center;justify-content:center}
.pager{display:flex;gap:5px;align-items:center}
.pager i{width:6px;height:6px;border-radius:50%;background:var(--blue)}
.pager b{width:8px;height:8px;border-radius:50%;border:2px solid var(--blue)}
/* new arrival */
.arr-card{top:1923px;width:237px;height:349px;background:var(--white);box-shadow:3px 4px 8px rgba(0,0,0,.14);display:flex;flex-direction:column;align-items:center}
.arr-card.on{border:2px solid var(--blue)}
.arr-card .pic{margin-top:45px;width:78px;height:183px}
.stars{margin-top:22px;color:var(--star);font-size:15px;letter-spacing:4px}
.arr-card h5{margin-top:12px;font-size:33px;line-height:1}
.round{width:48px;height:48px;border-radius:50%;display:flex;align-items:center;justify-content:center}
.round.light{background:#e7eef6}
.round.solid{background:var(--blue)}
/* products offered */
.offer{top:2449px;height:269px;background:var(--white);box-shadow:0 4px 10px rgba(0,0,0,.12)}
.offer h3{font-size:33px;line-height:1}
.offer .range{font-size:24px;margin-top:16px;line-height:1}
.offer p{font-size:10.5px;margin-top:16px}
.offer .add{margin-top:16px;width:134px;height:32px}
/* newsletter */
.footer{top:2948px;left:0;width:1200px;height:467px;background:var(--footer)}
.news{left:119px;top:2873px;width:961px;height:185px;background-color:var(--blue);background-image:radial-gradient(rgba(255,255,255,.18) 1.5px,transparent 1.6px);background-size:12px 12px}
.news h3{position:absolute;left:54px;top:72px;color:var(--white);font-size:38px;line-height:.82}
.news form{position:absolute;left:498px;top:77px;width:398px;height:36px;display:flex;background:var(--white);border:1px solid #cfe0f2}
.news .email{flex:1;background:var(--blue);border:1px solid rgba(255,255,255,.7);color:#d7e7f8;font-size:10px;display:flex;align-items:center;padding-left:15px}
.news .sub{width:123px;display:flex;align-items:center;justify-content:center;color:var(--blue);font-weight:600;font-size:13px}
/* footer */
.f-col{color:var(--white);font-size:14px;line-height:22px}
.f-col h4{font-size:30px;line-height:1;margin-bottom:6px}
.f-col .wordmark{color:var(--white);font-size:25px;line-height:36px}
.f-div{width:1px;height:120px;background:#777}
.socials{display:flex;gap:6px}
.socials i{width:33px;height:33px;border:1.5px solid var(--white);border-radius:50%;display:block}
.pay{display:flex;gap:6px}
.pay i{width:32px;height:20px;border-radius:3px;display:block}
.bottom{top:3415px;left:0;width:1200px;height:41px;background:var(--footer-deep);color:#e6e6e6;font-size:13px;display:flex;align-items:center;justify-content:center}
.bottom b{color:var(--white);margin:0 6px 0 4px}
</style>
</head>
<body>

<div class="abs topbar">
  <span><svg width="14" height="9" viewBox="0 0 14 9"><rect x=".5" y=".5" width="8" height="6" fill="none" stroke="#222"/><path d="M8.5 3h3l2 2v1.5h-5z" fill="none" stroke="#222"/><circle cx="3" cy="7.5" r="1.2" fill="#222"/><circle cx="11" cy="7.5" r="1.2" fill="#222"/></svg>Free Shipping Over $299</span>
  <span><svg width="12" height="9" viewBox="0 0 12 9"><rect x=".5" y=".5" width="11" height="8" fill="none" stroke="#222"/><path d="M.5.5 6 5l5.5-4.5" fill="none" stroke="#222"/></svg>info@topwavegoods.com &nbsp;&nbsp;<svg width="10" height="10" viewBox="0 0 10 10"><path d="M2 1l2 2-1 1.5c.8 1.5 1.5 2.2 3 3L7.5 6l2 2-1.5 1.5C4.5 9 1 5.5.5 2z" fill="none" stroke="#222" stroke-width=".8"/></svg>555 010-2288 CA</span>
</div>

<header class="abs header">
  <div class="wordmark">Top Wave Goods</div>
  <div class="search">
    <div class="cat">All Categories <svg width="9" height="6" viewBox="0 0 9 6"><path d="M1 1l3.5 3.5L8 1" fill="none" stroke="#333" stroke-width="1.5"/></svg></div>
    <div class="field">Search</div>
    <div class="go"><svg width="12" height="12" viewBox="0 0 12 12"><circle cx="5" cy="5" r="4" fill="none" stroke="#222" stroke-width="1.3"/><path d="M8 8l3 3" stroke="#222" stroke-width="1.3"/></svg></div>
  </div>
  <div class="icons">
    <svg width="18" height="18" viewBox="0 0 18 18"><path d="M9 15S2 10.5 2 6a3.5 3.5 0 0 1 7-1 3.5 3.5 0 0 1 7 1c0 4.5-7 9-7 9z" fill="none" stroke="#222" stroke-width="1.5"/></svg>
    <svg width="18" height="18" viewBox="0 0 18 18"><path d="M1 2h3l2 9h9l2-6H5" fill="none" stroke="#222" stroke-width="1.5"/><circle cx="7" cy="15" r="1.3" fill="#222"/><circle cx="14" cy="15" r="1.3" fill="#222"/></svg>
    <svg width="18" height="18" viewBox="0 0 18 18"><path d="M4 13V8a5 5 0 0 1 10 0v5l1.5 1.5h-13zM7.5 16h3" fill="none" stroke="#222" stroke-width="1.5"/></svg>
    <svg width="18" height="18" viewBox="0 0 18 18"><circle cx="9" cy="6" r="3.5" fill="none" stroke="#222" stroke-width="1.5"/><path d="M2.5 17a6.5 6.5 0 0 1 13 0" fill="none" stroke="#222" stroke-width="1.5"/></svg>
  </div>
</header>

<nav class="abs nav">
  <span class="active">Home</span><span>EMF Protection Devices ⌄</span><span>Options ⌄</span><span>Recommendations ⌄</span><span>Newsletter ⌄</span><span>Products ⌄</span><span>About Us ⌄</span>
</nav>

<section class="abs hero" role="img" aria-label="Flat-lay photo of headphones, a speaker and a laptop sleeve with protective stickers applied"></section>
<div class="abs hero-kicker">FOR ALL ELECTRONICS</div>
<h1 class="abs hero-title display">EMF PRODUCTS</h1>
<p class="abs hero-text">As EMF sensitives and medical researchers, we offer a select group of products that works best for us</p>
<a class="abs btn hero-btn">View All Products <svg width="11" height="9" viewBox="0 0 11 9"><path d="M0 4.5h9M6 1l3.5 3.5L6 8" fill="none" stroke="#fff" stroke-width="1.5"/></svg></a>
<div class="abs hero-dots"><i></i><i></i><b></b></div>

<section class="abs features">
  <div class="feature">
    <svg width="62" height="44" viewBox="0 0 62 44"><path d="M14 6h28v26H14zM42 14h10l7 9v9H42z" fill="none" stroke="#2f80cf" stroke-width="3"/><circle cx="22" cy="35" r="5" fill="#fff" stroke="#2f80cf" stroke-width="3"/><circle cx="50" cy="35" r="5" fill="#fff" stroke="#2f80cf" stroke-width="3"/><path d="M2 14h9M5 21h6M2 28h9" stroke="#2f80cf" stroke-width="3"/></svg>
    <div><h4 class="display">FREE SHIPPING OVER $299</h4><p>Unlock free shipping on orders exceeding $299</p></div>
  </div>
  <div class="feature">
    <svg width="58" height="56" viewBox="0 0 58 56"><path d="M10 14A23 23 0 1 1 6 30" fill="none" stroke="#2f80cf" stroke-width="3"/><path d="M4 6v10h10" fill="none" stroke="#2f80cf" stroke-width="3"/><path d="M19 22l11-6 11 6v13l-11 6-11-6zM19 22l11 6 11-6M30 28v13" fill="none" stroke="#2f80cf" stroke-width="2.5"/></svg>
    <div><h4 class="display">90 DAY RETURNS</h4><p>Hassle-Free Satisfaction Guaranteed</p></div>
  </div>
  <div class="feature">
    <svg width="68" height="56" viewBox="0 0 68 56"><path d="M10 30a24 24 0 0 1 48 0" fill="none" stroke="#2f80cf" stroke-width="3"/><rect x="5" y="26" width="9" height="16" rx="3" fill="none" stroke="#2f80cf" stroke-width="3"/><rect x="54" y="26" width="9" height="16" rx="3" fill="none" stroke="#2f80cf" stroke-width="3"/><path d="M20 24h28v18H32l-7 6v-6h-5z" fill="none" stroke="#2f80cf" stroke-width="3"/><circle cx="28" cy="33" r="2" fill="#2f80cf"/><circle cx="34" cy="33" r="2" fill="#2f80cf"/><circle cx="40" cy="33" r="2" fill="#2f80cf"/></svg>
    <div><h4 class="display">NEED HELP? CONTACT US</h4><p>Get In Touch with Our Support Team</p></div>
  </div>
</section>

<h2 class="abs sec-title display" style="top:768px">SHOP BY CATEGORIE</h2>
<div class="abs sec-rule" style="top:808px"></div>

<div class="abs cat-card" style="left:89px"><div class="cat-pack" role="img" aria-label="Orange sticker card package" style="background:linear-gradient(180deg,#f7941d,#f26522)"></div></div>
<div class="abs cat-card" style="left:349px"><div class="cat-pack" role="img" aria-label="White pet sticker package" style="background:linear-gradient(180deg,#f4f4f4,#d9d9d9)"></div></div>
<div class="abs cat-card" style="left:610px"><div class="cat-pack" role="img" aria-label="Teal aqua sticker package" style="background:linear-gradient(180deg,#2fa3a3,#174f6b)"></div></div>
<div class="abs cat-card" style="left:871px"><div class="cat-pack" role="img" aria-label="Green space sticker multipack" style="background:linear-gradient(180deg,#5fbf86,#2a7a52)"></div></div>
<div class="abs cat-name display" style="left:89px">SMART CARDS</div>
<div class="abs cat-name display" style="left:349px">PET PEBS</div>
<div class="abs cat-name display" style="left:610px">AQUA PEBS</div>
<div class="abs cat-name display" style="left:871px">SPACE PEBS</div>
<a class="abs btn explore">Explore More <svg width="11" height="9" viewBox="0 0 11 9"><path d="M0 4.5h9M6 1l3.5 3.5L6 8" fill="none" stroke="#fff" stroke-width="1.5"/></svg></a>

<h2 class="abs sec-title display" style="top:1338px">STARTER PACKAGES</h2>
<div class="abs sec-rule" style="top:1384px"></div>

<article class="abs pack" style="left:0;width:595px;background:linear-gradient(90deg,#2a2a2a 0%,#6b6b6b 35%,#8a8a8a 100%)" role="img" aria-label="Pendant tag on a cord resting on a wooden table">
  <div class="inner">
    <h3 class="display">TAG-STARTER PACKAGE</h3>
    <div class="price display">$69.95 <s>$119.00</s></div>
    <ul><li>Includes the <b>Body/Bio PEB</b> embedded in the <b>TAG</b> for you to wear or keep near you to strengthen and balance your energy field.</li><li>Plus <b>1 Bright PEB Set</b>-For your cell phone</li></ul>
    <a class="add">ADD TO CARD</a>
  </div>
</article>
<article class="abs pack" style="left:608px;width:592px;background:linear-gradient(90deg,#4a4a4a 0%,#7a7a7a 55%,#9a8f8c 100%)" role="img" aria-label="Wristband with a sticker worn on a wrist">
  <div class="inner" style="left:44px">
    <h3 class="display">WRISTBAND-STARTER PACKAGE</h3>
    <div class="price display">$69.95 <s>$110.00</s></div>
    <ul><li>Includes the <b>Body/Bio PEB</b> embedded in the <b>wristBAND</b> for you to wear or keep near you to strengthen and balance your energy field.</li><li>Plus <b>1 Bright PEB Set</b>-For your cell phone</li></ul>
    <a class="add">ADD TO CARD</a>
  </div>
</article>
<div class="abs pager" style="left:580px;top:1786px"><i></i><i></i><i></i><b></b></div>

<h2 class="abs sec-title display" style="top:1841px">NEW ARRIVAL</h2>
<div class="abs sec-rule" style="top:1889px"></div>

<div class="abs round light" style="left:89px;top:2064px"><svg width="20" height="14" viewBox="0 0 20 14"><path d="M19 7H2M8 1L2 7l6 6" fill="none" stroke="#222" stroke-width="2"/></svg></div>
<div class="abs arr-card" style="left:211px"><div class="pic" role="img" aria-label="Clip product package" style="background:linear-gradient(180deg,#f2f2f2,#cfcfcf)"></div><div class="stars">★★★★★</div><h5 class="display">PET PEBS</h5></div>
<div class="abs arr-card on" style="left:480px"><div class="pic" role="img" aria-label="Clip product package" style="background:linear-gradient(180deg,#f2f2f2,#cfcfcf)"></div><div class="stars">★★★★★</div><h5 class="display">CLIPS</h5></div>
<div class="abs arr-card" style="left:752px"><div class="pic" role="img" aria-label="Red wristband package" style="background:linear-gradient(180deg,#e5382b,#b81e22)"></div><div class="stars">★★★★★</div><h5 class="display">WRIST BAND</h5></div>
<div class="abs round solid" style="left:1062px;top:2064px"><svg width="20" height="14" viewBox="0 0 20 14"><path d="M1 7h17M12 1l6 6-6 6" fill="none" stroke="#fff" stroke-width="2"/></svg></div>

<h2 class="abs sec-title display" style="top:2368px;left:16px">PRODUCTS OFFERED</h2>
<div class="abs sec-rule" style="top:2416px;left:576px"></div>

<article class="abs offer" style="left:0;width:192px">
  <div style="position:absolute;right:64px;top:74px;white-space:nowrap"><h3 class="display">TO 4 DEVICES</h3></div>
  <p style="position:absolute;right:104px;top:126px;margin:0;white-space:nowrap">ated at checkout</p>
</article>
<article class="abs offer" style="left:243px;width:721px">
  <div role="img" aria-label="Fingers holding an orange round sticker" style="position:absolute;left:0;top:0;width:338px;height:269px;background:linear-gradient(120deg,#d9d4cf,#e9a36b 55%,#bfb6ad)"></div>
  <div style="position:absolute;left:375px;top:74px">
    <h3 class="display">BRIGHT PEBS- 1 TO 4 DEVICES</h3>
    <div class="range display">$49.95 - $124.95</div>
    <p>Taxes and shipping calculated at checkout</p>
    <a class="btn add">Add to Card</a>
  </div>
</article>
<div class="abs offer" style="left:1013px;width:187px;background:linear-gradient(135deg,#c2a27c,#e5e0d8 50%,#2a2a2a)" role="img" aria-label="Desk scene with a succulent, a laptop and a phone carrying stickers"></div>
<div class="abs round" style="left:214px;top:2550px;background:#f0f0f0;box-shadow:0 2px 6px rgba(0,0,0,.15)"><svg width="20" height="14" viewBox="0 0 20 14"><path d="M19 7H2M8 1L2 7l6 6" fill="none" stroke="#222" stroke-width="2"/></svg></div>
<div class="abs round solid" style="left:937px;top:2553px"><svg width="20" height="14" viewBox="0 0 20 14"><path d="M1 7h17M12 1l6 6-6 6" fill="none" stroke="#fff" stroke-width="2"/></svg></div>

<footer class="abs footer"></footer>
<section class="abs news">
  <h3 class="display">DON'T MISS OUT! SIGN UP<br>FOR OUR NEWSLETTER TODAY</h3>
  <form><div class="email">Enter Your Email</div><div class="sub">Subscribe</div></form>
</section>

<div class="abs f-col" style="left:88px;top:3155px">
  <div class="wordmark">Top Wave Goods</div>
  <p style="margin-top:10px;font-size:13.5px;line-height:21px">Helena Marsh, CLS, NCMP, Ph.D.<br>Medical Researcher / EMF-Sensitive<br>Dorian Marsh, Ph.D.</p>
  <h4 class="display" style="font-size:22px;margin-top:14px">FOLLOW US :</h4>
  <div class="socials"><i></i><i></i><i></i><i></i></div>
</div>
<div class="abs f-div" style="left:380px;top:3216px"></div>
<div class="abs f-col" style="left:421px;top:3150px">
  <h4 class="display">QUICK LINK</h4>
  Home<br>EMF Protection<br>Devices<br>Options<br>Recommendations<br>Newsletter<br>Savings
</div>
<div class="abs f-div" style="left:601px;top:3216px"></div>
<div class="abs f-col" style="left:645px;top:3150px">
  <h4 class="display">SUPPORT</h4>
  Contact Us<br>Refund Policy<br>Terms of Service<br>Privacy Policy
  <div class="display" style="font-size:21px;line-height:22px;margin:18px 0 0 -23px">FREE SHIPPING OVER<br>$299 180-DAY RETURNS</div>
</div>
<div class="abs f-div" style="left:807px;top:3216px"></div>
<div class="abs f-col" style="left:851px;top:3150px">
  <h4 class="display">CONTACT</h4>
  <div style="padding-left:2px"><span style="color:var(--blue)">●</span>&nbsp; 555 010-2288 Fairview, CA<br><span style="color:var(--blue)">●</span>&nbsp; info@topwavegoods.com<br><span style="color:var(--blue)">●</span>&nbsp; Clearfield Wellness Consulting LLC</div>
  <h4 class="display" style="margin-top:14px">WE ACCEPT</h4>
  <div class="pay"><i style="background:#fff"></i><i style="background:#1a3c8f"></i><i style="background:#fff"></i><i style="background:#fff"></i><i style="background:#2e77bc"></i></div>
</div>

<div class="abs bottom">© 2024 <b>TOPWAVEGOODS</b>| All rights reserved</div>

</body>
</html>
```